Bright Meadow Lodge website (design only)

Bright Meado Lodge (http://www.brightmeadowmw.example) is a private Safari lodge located in Malawi.
We would like a modern, professional website designed that does not subscribe to the cliched view of a Safari in Africa, but still maintain a wildlife/safari atmosphere.

The aim of our website is to entice people & drive them to the booking form.

Here are some examples of websites that we like. Although we would like our site to be a bit more in line with modern web design trends.

http://www.korumelo.example/
http://www.tarvonel.example/
http://www.plovandetri.example/

Requirements
Must have
• Here is a list of the pages required. Most of them will follow a standard content layout. I.e. heading, body and images.

If you take a look at the website, you will get an idea of hoe many page types there are +- 5

http://www.brightmeadowmw.example/index.htm

About Bright Meadow
Ulkoro Country Club
Rooms
Conferences
Cuisine
Facilities
Your Safari
Activities
Rates & Special Offers
Booking form
Latest Developments
How To Get There
Gallery
Contact Us
Blog / Newsfeed

```html
<!DOCTYPE html>
<html lang="en">
<head>
<meta charset="utf-8">
<title>Bright Meadow Lodge</title>
<link rel="stylesheet" href="https://fonts.googleapis.com/css2?family=Federo&family=Josefin+Sans:wght@600&family=Arimo:wght@400;700&display=swap">
<style>
:root{
  --bg:#262626;
  --bar:#3a3b32;
  --nav-active:#111111;
  --nav-text:#d6d6d0;
  --gold:#c9a566;
  --tan:#c8b489;
  --body:#a9a9a1;
  --rule:#3d3d3b;
  --frame:#9a9a94;
  --footer-text:#b9b9ad;
}
*{margin:0;padding:0;box-sizing:border-box}
html,body{width:1200px;height:972px;overflow:hidden;background:var(--bg)}
body{position:relative;font-family:"Arimo",Arial,sans-serif;color:var(--body)}
.masthead{position:absolute;left:43px;top:26px;display:flex;align-items:baseline;gap:26px;white-space:nowrap}
.brand{font-family:"Federo",serif;font-size:36px;color:var(--tan);letter-spacing:.3px}
.tagline{font-family:"Josefin Sans",sans-serif;font-weight:600;font-size:14.5px;color:var(--tan)}
.social{position:absolute;top:0;right:40px;display:flex;height:34px}
.social span{width:47px;height:26px;border-left:1px solid #4a4a48;display:flex;align-items:center;justify-content:center}
.main-nav{position:absolute;left:39px;top:105px;width:1121px;height:35px;display:flex;justify-content:space-between;font-size:14px;color:var(--nav-text)}
.main-nav a{color:inherit;text-decoration:none;padding:0 6px;line-height:35px;white-space:nowrap}
.main-nav a.active{background:var(--nav-active);color:#fff;padding:0 10px}
.hero{position:absolute;left:36px;top:140px;width:1124px;height:358px;background:linear-gradient(180deg,#3a4048 0%,#5d7183 35%,#8f8a72 70%,#b8894a 88%,#6b5530 100%)}
.card{position:absolute;top:526px;width:251px}
.thumb{display:block;width:251px;height:97px;border:1px solid var(--frame);padding:2px;background-clip:content-box}
.card h2,.feature h2{font-size:14px;font-weight:700;color:var(--gold);text-transform:uppercase;margin-top:17px;letter-spacing:.1px;white-space:nowrap}
.card p,.feature p{font-size:12.6px;line-height:16.4px;margin-top:5px;width:250px}
.divider{position:absolute;width:1px;background:var(--rule)}
.feature{position:absolute;top:798px}
.booking-banner{position:absolute;left:617px;top:808px;width:541px;height:96px;border:1px solid var(--frame);padding:2px;background-clip:content-box}
.booking-banner span{position:absolute;right:22px;bottom:8px;font-family:"Federo",serif;font-size:19px;color:#e8e2d0}
.footer{position:absolute;left:0;top:941px;width:1200px;height:31px;background:var(--bar);font-size:11.5px;color:var(--footer-text);text-align:right;padding:9px 40px 0 0}
</style>
</head>
<body>
<header>
  <div class="masthead">
    <div class="brand">Bright Meadow Lodge</div>
    <div class="tagline">Velamo Estate | Kirundwe</div>
  </div>
  <nav class="social" aria-label="Social links">
    <span><svg width="14" height="14"><circle cx="7" cy="7" r="6" fill="#8a8a86"/></svg></span>
    <span><svg width="14" height="14"><circle cx="7" cy="7" r="6" fill="#8a8a86"/></svg></span>
    <span><svg width="14" height="14"><circle cx="7" cy="7" r="6" fill="#8a8a86"/></svg></span>
    <span><svg width="18" height="13" viewBox="0 0 18 13"><rect x="1" y="1" width="16" height="11" fill="#8a8a86"/><path d="M1 1 L9 7 L17 1" fill="none" stroke="#262626" stroke-width="1.5"/></svg></span>
  </nav>
  <nav class="main-nav">
    <a class="active" href="#">Home</a><a href="#">About</a><a href="#">Gallery</a><a href="#">Safari</a><a href="#">Activities</a><a href="#">Rooms</a><a href="#">Cuisine</a><a href="#">Conferences</a><a href="#">Facilities</a><a href="#">Rates &amp; Specials</a><a href="#">Bookings</a><a href="#">Developments</a><a href="#">How To Get There</a><a href="#">Blog</a><a href="#">Contact Us</a>
  </nav>
</header>

<div class="hero" role="img" aria-label="Giraffe walking across grassland under a dramatic sunset sky"></div>

<section class="card" style="left:36px">
  <div class="thumb" role="img" aria-label="Two zebras side by side" style="background:linear-gradient(90deg,#6d6d6d,#d8d8d8,#5a5a5a,#cfcfcf)"></div>
  <h2>Bright Meadow Lodge</h2>
  <p>Warmest welcome to the unique Malawi experience: lodge complex, game park, the 18 hole Ulkoro golf club &amp; Tesano dam. Bright Meadow Lodge provides all the holiday and business prerequisites in a beautiful, relaxing, quiet and secure environment.</p>
</section>
<div class="divider" style="left:305px;top:526px;height:240px"></div>
<section class="card" style="left:326px">
  <div class="thumb" role="img" aria-label="Two impala antelopes" style="background:linear-gradient(90deg,#3e4a28,#a8743c,#c99a5c,#55602e)"></div>
  <h2>Game &amp; Wild Birds</h2>
  <p>Lorem ipsum dolor sit amet, consectetuer adipiscing elit, sed diam nonummy nibh euismod tincidunt ut laoreet dolore magna aliquam erat volutpat. Ut wisi enim ad minim veniam quis nostrud exerci tatin ullamcorper suscipit lobortis nisl ut aliquip ex ea comod.</p>
</section>
<div class="divider" style="left:597px;top:526px;height:240px"></div>
<section class="card" style="left:617px">
  <div class="thumb" role="img" aria-label="Lodge lounge with red sofas" style="background:linear-gradient(90deg,#8c2a24,#c9b08a,#5a3020,#a0441f)"></div>
  <h2>The Lodge &amp; Rooms</h2>
  <p>Lorem ipsum dolor sit amet, consectetuer adipiscing elit, sed diam nonummy nibh euismod tincidunt ut laoreet dolore magna aliquam erat volutpat. Ut wisi enim ad minim veniam quis nostrud exerci tatin ullamcorper suscipit lobortis nisl ut aliquip ex ea comod.</p>
</section>
<div class="divider" style="left:888px;top:526px;height:240px"></div>
<section class="card" style="left:908px">
  <div class="thumb" role="img" aria-label="Conference room set with tables" style="background:linear-gradient(90deg,#d9d4cc,#9c2c3c,#e0dad2,#6a4a3a)"></div>
  <h2>Conference &amp; Resturant</h2>
  <p>Lorem ipsum dolor sit amet, consectetuer adipiscing elit, sed diam nonummy nibh euismod tincidunt ut laoreet dolore magna aliquam erat volutpat. Ut wisi enim ad minim veniam quis nostrud exerci tatin ullamcorper suscipit lobortis nisl ut aliquip ex ea comod.</p>
</section>

<section class="feature" style="left:36px">
  <h2>Bright Meadow Activities</h2>
  <p>18 Hole Golf Course, Guided Walks, Game Drives, Bird Watching, Fishing, Sailing, Swimming Pool, Bushwalking, Hiking, and Trekking.</p>
</section>
<div class="divider" style="left:308px;top:808px;height:86px"></div>
<section class="feature" style="left:330px">
  <h2>Safari Wildlife</h2>
  <p>Giraffe, Sable and their newbord calves, Waterbuck, Zebra, Impala, Wildebeest, Nyala and numerous duiker and smaller wild cats and otter</p>
</section>
<a class="booking-banner" href="#" role="img" aria-label="Herd of impala at a waterhole" style="background:linear-gradient(180deg,#4e5a2a,#a07a3c 55%,#3a4a3a)"><span>. . . enquire for a booking</span></a>

<footer class="footer">2012 © www.brightmeadowmw.example | All rights reserved</footer>
</body>
</html>
```